CV Template

We need a graphic design to our new CV templates for our consultants. We are a small young Danish upcoming IT-business company making software solutions for our customers etc. You can visit our new website here: dev.solbakken-data.com, then you can see our web design, colors etc. I have attached a file for your inspiration :-) In the presentation I would like to have a picture of the employee, some text who descripe the profile/consultant and then I imagine that there is a table where we can write the employee's skills etc.

I would like the design to be "fresh & catchy" :-)

Looking forward to hear from you.

Best regards,
Birgit

```html
<!DOCTYPE html>
<html lang="en">
<head>
<meta charset="utf-8">
<title>Consultant CV – Past Projects</title>
<link href="https://fonts.googleapis.com/css2?family=Carlito:wght@400;700&display=swap" rel="stylesheet">
<style>
  :root {
    --page-bg: #eef2f7;
    --panel-bg: #ffffff;
    --accent: #1a73c0;
    --rule: #8fb8de;
    --text: #333333;
    --brand: #7d8ba0;
    --footer-text: #1d1d1d;
  }
  * { margin: 0; padding: 0; box-sizing: border-box; }
  html, body { width: 902px; height: 1200px; overflow: hidden; }
  body {
    position: relative;
    background: var(--page-bg);
    font-family: "Carlito", "Calibri", sans-serif;
    color: var(--text);
  }
  .brand {
    position: absolute; top: 40px; left: 690px;
    font-size: 24px; font-weight: 400; color: var(--brand);
    letter-spacing: 0.5px; white-space: nowrap;
  }
  .sheet {
    position: absolute; left: 66px; top: 142px;
    width: 794px; height: 984px;
    background: var(--panel-bg); border-radius: 42px;
  }
  .abs { position: absolute; white-space: nowrap; }
  .section-title {
    font-size: 20px; font-weight: 700; color: var(--accent);
  }
  .rule { position: absolute; height: 1px; background: var(--rule); }
  .intro { font-size: 12.5px; }
  .cell { font-size: 12.5px; }
  .desc { font-size: 12.5px; line-height: 18px; width: 360px; white-space: normal; }
  .closing { font-size: 20px; font-weight: 700; color: var(--accent); }
  .footer {
    position: absolute; top: 1136px; left: 0; width: 902px;
    font-size: 12.5px; font-weight: 700; color: var(--footer-text);
  }
  .footer span { position: absolute; white-space: nowrap; }
</style>
</head>
<body>
  <div class="brand">Solbakken Data</div>

  <main class="sheet"></main>

  <section class="projects">
    <h2 class="abs section-title" style="left:96px; top:202px;">Past Projects</h2>
    <div class="rule" style="left:96px; top:228px; width:718px;"></div>
    <p class="abs intro" style="left:96px; top:232px;">Jonas has gained extensive experience through various past projects as listed below:</p>

    <h3 class="abs section-title" style="left:96px; top:278px;">Date</h3>
    <div class="rule" style="left:94px; top:303px; width:146px;"></div>
    <h3 class="abs section-title" style="left:265px; top:278px;">Role</h3>
    <div class="rule" style="left:262px; top:304px; width:147px;"></div>
    <h3 class="abs section-title" style="left:448px; top:281px;">Description of achievement</h3>
    <div class="rule" style="left:445px; top:306px; width:364px;"></div>

    <p class="abs cell" style="left:96px; top:309px;">Feb 2002 – Mar 2004</p>
    <p class="abs cell" style="left:265px; top:309px;">Programming</p>
    <p class="abs desc" style="left:448px; top:311px;">Adasd asdasdasdv adfadfw asfaae wgdfervsdv xcv. Aefrwevsdv,bdfbertgdbbcvb dfbsv. Adasd asdasdasdv adfadfw asfaae wgdfervsdv xcv. Aefrwevsdv,bdfbertgdbbcvb dfbsv.</p>

    <p class="abs cell" style="left:96px; top:363px;">Feb 2002 – Mar 2004</p>
    <p class="abs cell" style="left:265px; top:363px;">Supervisor</p>
    <p class="abs desc" style="left:448px; top:374px;">Adasd asdasdasdv adfadfw asfaae wgdfervsdv xcv. Aefrwevsdv,bdfbertgdbbcvb dfbsv. Adasd asdasdasdv adfadfw asfaae wgdfervsdv xcv.</p>

    <p class="abs cell" style="left:96px; top:444px;">Feb 2002 – Mar 2004</p>
    <p class="abs cell" style="left:265px; top:445px;">Project head</p>
    <p class="abs desc" style="left:448px; top:439px;">Adasd asdasdasdv adfadfw asfaae wgdf.ervsdv xcv. Aefrwevsdv,bdfbertgdbbcvb dfbsv. Adasd asdasdasdv adfadfw asfaae wgdfervsdv xcv. Aefrwevsdv,bdfbertgdbbcvb dfbsv. dasd asdasdasdv adfadfw asfaae wgdfervsdv xcv. efrwevsdv,bd fbertgdbbcvb dfbsv.</p>
  </section>

  <div class="rule" style="left:111px; top:591px; width:721px;"></div>
  <p class="abs closing" style="left:0; width:944px; text-align:center; top:594px;">The End</p>
  <div class="rule" style="left:111px; top:621px; width:721px;"></div>

  <footer class="footer">
    <span style="left:108px;">Solbakken Data ApS</span>
    <span style="left:240px;">Lærkevej 12</span>
    <span style="left:336px;">2200 København N.</span>
    <span style="left:468px;">Tel: +45 20 30 40 50</span>
    <span style="left:610px;">www.solbakken-data.dk</span>
  </footer>
</body>
</html>
```